Achei a plataforma de serviços genial. Quanto maior o número de designers envolvidos no projeto, tanto mais diversas e criativas se mostram as soluções.

```html
<!DOCTYPE html>
<html lang="pt-BR">
<head>
<meta charset="utf-8">
<title>Porto Alto — Cartão de Visita</title>
<link href="https://fonts.googleapis.com/css2?family=Cinzel:wght@400&family=Open+Sans:ital,wght@0,400;1,400&display=swap" rel="stylesheet">
<style>
  :root {
    --backdrop: #1b1b1d;
    --card: #fbfbfb;
    --navy: #233068;
    --divider: #d4d6dc;
    --ink-soft: #4a5480;
  }
  * { box-sizing: border-box; margin: 0; padding: 0; }
  html, body {
    width: 1200px; height: 1200px; overflow: hidden;
    background: var(--backdrop);
  }
  .canvas {
    width: 1200px; height: 1200px;
    display: flex; align-items: center; justify-content: center;
  }
  .business-card {
    width: 1000px; height: 572px;
    background: var(--card);
    display: grid;
    grid-template-columns: 470px 1px 1fr;
    align-items: stretch;
    box-shadow: 0 20px 50px rgba(0,0,0,.45);
  }
  .brand {
    display: flex; align-items: center; justify-content: center;
    padding: 0 40px;
  }
  .brand-name {
    display: flex; align-items: center; gap: 14px;
    white-space: nowrap;
    font-family: "Open Sans", sans-serif; font-weight: 400;
    font-size: 44px; color: var(--navy);
  }
  .brand-mark {
    width: 18px; height: 18px; border-radius: 50%;
    background: var(--navy);
  }
  .divider {
    background: var(--divider);
    margin: 70px 0;
  }
  .details {
    padding: 90px 50px 0 44px;
  }
  .person-name {
    font-family: "Cinzel", serif; font-weight: 400;
    font-size: 36px; color: var(--navy); letter-spacing: 1px;
    white-space: nowrap;
  }
  .person-role {
    font-family: "Cinzel", serif;
    font-size: 13px; letter-spacing: 7px; color: var(--navy);
    margin-top: 2px;
  }
  .contact-list { list-style: none; margin-top: 38px; }
  .contact-item {
    display: flex; gap: 12px; align-items: flex-start;
    font-family: "Open Sans", sans-serif; font-style: italic;
    font-size: 14.5px; line-height: 1.55; color: var(--ink-soft);
    margin-bottom: 22px;
  }
  .contact-icon { flex: 0 0 16px; width: 16px; height: 16px; margin-top: 3px; }
  .contact-icon * { fill: none; stroke: var(--navy); stroke-width: 1.6; }
</style>
</head>
<body>
<main class="canvas">
  <section class="business-card">
    <div class="brand">
      <div class="brand-name"><span class="brand-mark"></span>Porto Alto</div>
    </div>
    <div class="divider"></div>
    <div class="details">
      <h1 class="person-name">Rafael Monteiro</h1>
      <p class="person-role">SÓCIO</p>
      <ul class="contact-list">
        <li class="contact-item">
          <svg class="contact-icon" viewBox="0 0 16 16"><path d="M8 15s5-5.2 5-8.5A5 5 0 0 0 3 6.5C3 9.8 8 15 8 15z"/><circle cx="8" cy="6.5" r="1.8"/></svg>
          <span>Porto Alto Consultoria e Assessoria Empresarial Ltda<br>Rua das Acácias, 240 - Vila Serena<br>CEP 01234-000 - São Paulo - SP - Brasil</span>
        </li>
        <li class="contact-item">
          <svg class="contact-icon" viewBox="0 0 16 16"><path d="M4 1.5h3l1 3.5-2 1.3a8 8 0 0 0 3.7 3.7l1.3-2 3.5 1v3A1.5 1.5 0 0 1 13 14.5 11.5 11.5 0 0 1 1.5 3 1.5 1.5 0 0 1 3 1.5z"/></svg>
          <span>Tel.: +55 (11) 90000-1234</span>
        </li>
        <li class="contact-item">
          <svg class="contact-icon" viewBox="0 0 16 16"><rect x="1.5" y="3.5" width="13" height="9" rx="1"/><path d="M1.5 4l6.5 5 6.5-5"/></svg>
          <span>rafael.monteiro@portoalto.com.br</span>
        </li>
      </ul>
    </div>
  </section>
</main>
</body>
</html>
```